Dog breeder design card

A card for our dog showing/breeding and companion puppy buyers.
Updates

Project Deadline Extended
Reason: The photo's I provided were not seen by designers because of a glitch or error, so I will need to start them over again in the designs submitted to me. I uploaded and emailed the photo's last night.

Thank you all so much for your lovely designs, I like wquite a few of them. I provided images in my original brief, but these apparently did not become available for you to see. I have emailed my images now, so hopefully you may be able to incorporate them into your designs.

Thank you so much for your time,
kind regards,
Beatrice

I have attached the photo’s that can hopefully be incorporated onto my business card. I don’t mind if the whole images aren’t used, but maybe a soft focus look around the adult dog and in a corner of the card maybe....if that’s possible.

Contact Information for Business Card

Kestamor Bullmastiffs, adored by Gerald and Beatrice Lindqvist.
Hollowbrae VIC
0497 358614

Requirements
Nice to have
• Soft focus look to the outline of adult dogs head incorporated into perhaps a corner of the card. Soft focus outline around pups perhaps.
I do really love hot pink and/or purple text if possible.
"Kestamor Bullmastiffs" to be incorporated on the front of card, our details on reverse.
Would prefer a glossy finish rather than matt.

```html
<!DOCTYPE html>
<html lang="en">
<head>
<meta charset="utf-8">
<title>Kestamor Bullmastiffs – Business Card</title>
<link href="https://fonts.googleapis.com/css2?family=Oswald:wght@600&family=Questrial&display=swap" rel="stylesheet">
<style>
  :root {
    --stage: #dcdcdc;
    --ink: #000000;
    --paper: #ffffff;
    --rose: #c4507a;
    --text: #1a1a1a;
  }
  html, body {
    margin: 0;
    padding: 0;
    width: 1200px;
    height: 848px;
    overflow: hidden;
    background: var(--stage);
  }
  .canvas {
    position: relative;
    width: 1200px;
    height: 848px;
  }
  .card {
    position: absolute;
    left: 331px;
    width: 538px;
    height: 307px;
    overflow: hidden;
  }
  .card--front {
    top: 85px;
    background: var(--ink);
  }
  .card--back {
    top: 455px;
    background: var(--paper);
  }
  .brand-mark {
    position: absolute;
    width: 110px;
    height: 110px;
    left: 214px;
    top: 62px;
    background: var(--paper);
  }
  .brand-name {
    position: absolute;
    margin: 0;
    font-family: 'Oswald', 'Arial Narrow', sans-serif;
    font-weight: 600;
    color: var(--rose);
    white-space: nowrap;
    line-height: 1;
  }
  .card--front .brand-name {
    left: 0;
    width: 100%;
    text-align: center;
    top: 186px;
    font-size: 30px;
  }
  .website {
    position: absolute;
    left: 0;
    width: 100%;
    top: 222px;
    text-align: center;
    font-family: 'Questrial', sans-serif;
    font-size: 14px;
    letter-spacing: 0.3px;
    color: var(--paper);
  }
  .card--back .brand-name {
    left: 37px;
    top: 42px;
    font-size: 40px;
  }
  .rule {
    position: absolute;
    left: 0;
    top: 90px;
    width: 390px;
    height: 1px;
    background: var(--rose);
  }
  .back-mark {
    position: absolute;
    left: 416px;
    top: 25px;
    width: 78px;
    height: 78px;
    background: var(--rose);
  }
  .person {
    position: absolute;
    left: 37px;
    top: 144px;
    font-family: 'Questrial', sans-serif;
  }
  .person__name {
    margin: 0;
    font-size: 30px;
    font-weight: 700;
    color: var(--rose);
    line-height: 1;
  }
  .person__role {
    margin: 1px 0 0;
    font-size: 18px;
    color: var(--text);
    line-height: 1;
  }
  .contact {
    position: absolute;
    left: 37px;
    top: 213px;
    margin: 0;
    font-family: 'Questrial', sans-serif;
    font-size: 18px;
    line-height: 1;
    color: var(--text);
  }
  .footer-band {
    position: absolute;
    left: 0;
    top: 279px;
    width: 538px;
    height: 28px;
    display: flex;
  }
  .footer-band__tagline {
    width: 390px;
    background: var(--ink);
    color: var(--paper);
    font-family: 'Questrial', sans-serif;
    font-weight: 700;
    font-size: 15px;
    letter-spacing: 0.3px;
    line-height: 28px;
    padding-left: 40px;
    box-sizing: border-box;
    white-space: nowrap;
  }
  .footer-band__accent {
    flex: 1;
    background: var(--rose);
  }
</style>
</head>
<body>
<main class="canvas">
  <section class="card card--front" aria-label="Card front">
    <div class="brand-mark"></div>
    <h1 class="brand-name">Kestamor Bullmastiffs</h1>
    <div class="website">www.kestamorbullmastiffs.com</div>
  </section>

  <section class="card card--back" aria-label="Card back">
    <h2 class="brand-name">Kestamor Bullmastiffs</h2>
    <div class="rule"></div>
    <div class="back-mark"></div>
    <div class="person">
      <p class="person__name">Beatrice Lindqvist</p>
      <p class="person__role">Owner</p>
    </div>
    <p class="contact">Hollowbrae VIC 0497 358614</p>
    <div class="footer-band">
      <div class="footer-band__tagline">adored by Gerald and Beatrice Lindqvist</div>
      <div class="footer-band__accent"></div>
    </div>
  </section>
</main>
</body>
</html>
```